New EZ Bag Modern design for Coral Tide

The frozen food category is growing, but the seafood frozen food aisle still needs an image overhaul. We have a high-quality product and we want an amazing package design to stand out as Modern, Honest, Happy, Healthy Coral Tide. Coral Tide offers a consistent superior quality shrimp. Sustainably farmed, no antibiotics ever, and responsibly sourced from Latin America (Ecuador), only from the world’s most advanced farms with the highest International Certifications. Coral Tide is peeled and packed in the U.S.A. After decades of experience in the global seafood industry and years of research and development, we built our state-of-the-art facility to bring automation and precision to every step of farmed shrimp processing.

Target Market(s)

We are targeting people that look for a great product in terms of flavor and texture. Customers that look for a product that is convenient, consistent, and healthy. Customers that look for brands that are transparent with their product and processes. Customers that want high-quality seafood at the reach of their hands, anytime.

Font styles to use
Sans Serif

Requirements
Must have
• Please read Brief.
Given the constraint we might have because of the freezers, it is essential to consider a high-impact clean design, with excellent legibility font size and coloring. The bag should communicate all our benefits from behind the glass. We want to show the real product, and there should be a window to clearly see what is inside the bag (I.Q.F. shrimp).
We want to use high-impact colors to stand compared to other products from the category (lots of white, blue, pink) and emphasize the brand.
Nice to have
• Strong, modern, clean fonts

```html
<!DOCTYPE html>
<html lang="en">
<head>
<meta charset="utf-8">
<title>Coral Tide – Cooked Shrimp Bag</title>
<link rel="stylesheet" href="https://fonts.googleapis.com/css2?family=Arimo:wght@400;700&family=Bowlby+One&family=Oswald:wght@600&display=swap">
<style>
  :root {
    --stage: #ececec;
    --bag-white: #f4f4f5;
    --seal: #e2e2e4;
    --seal-line: #cfcfd3;
    --brand-blue: #3d96d2;
    --deep-blue: #2a78bd;
    --pale-blue: #a7cbe2;
    --blush: #c8a4c6;
    --ink: #232323;
    --logo-grey: #3a3a3c;
    --cooked: #c9602a;
    --leaf: #4d9a3a;
    --badge-dark: #2e2e30;
  }
  * { box-sizing: border-box; margin: 0; padding: 0; }
  html, body { width: 1200px; height: 788px; overflow: hidden; }
  body { background: var(--stage); position: relative; font-family: "Arimo", Arial, sans-serif; }

  .bag {
    position: absolute; left: 350px; top: 34px;
    width: 500px; height: 720px;
    background: var(--bag-white);
    border-radius: 6px;
    overflow: hidden;
  }
  .bag__art { position: absolute; inset: 0; }

  .brand {
    position: absolute; left: 90px; top: 92px;
    display: flex; align-items: center; gap: 16px;
  }
  .brand__dot { width: 54px; height: 54px; border-radius: 50%; background: var(--cooked); }
  .brand__name {
    font-family: "Oswald", sans-serif; font-weight: 600;
    font-size: 58px; line-height: 0.95; letter-spacing: 2px;
    color: var(--logo-grey); text-transform: uppercase;
  }

  .tagline {
    position: absolute; left: 0; right: 0; top: 248px;
    text-align: center;
    font-family: "Bowlby One", sans-serif; font-size: 29px; line-height: 1.1;
    color: var(--ink); text-transform: uppercase;
  }

  .window {
    position: absolute; left: 160px; top: 340px;
    width: 200px; height: 200px;
    transform: rotate(45deg);
    border: 7px solid var(--brand-blue);
    border-radius: 34px;
    background: radial-gradient(circle at 45% 45%, #f6c7a9 0%, #ec9c78 45%, #f3d7c6 100%);
  }

  .cooked {
    position: absolute; left: 300px; top: 360px;
    padding: 2px 12px;
    background: #fff; border-radius: 14px;
    font-family: "Oswald", sans-serif; font-weight: 600;
    font-size: 44px; line-height: 1.05; color: var(--cooked);
  }

  .badge-natural {
    position: absolute; left: 52px; top: 370px;
    width: 76px; height: 76px; border-radius: 50%;
    background: var(--badge-dark);
    border: 4px solid #fff; box-shadow: 0 0 0 2px var(--badge-dark);
  }
  .badge-natural::after {
    content: ""; position: absolute; left: 20px; top: 18px;
    width: 32px; height: 32px; border-radius: 0 60% 0 60%;
    background: var(--leaf);
  }
  .badge-small {
    position: absolute; width: 46px; height: 46px; border-radius: 50%;
    background: #fff; border: 3px solid var(--badge-dark);
  }
  .badge-small--origin { left: 58px; top: 478px; }
  .badge-small--packed { left: 104px; top: 526px; }

  .flash {
    position: absolute; left: 314px; top: 470px;
    width: 172px; padding: 10px 8px 10px;
    background: var(--pale-blue); border-radius: 16px;
    text-align: center;
    font-weight: 700; font-size: 12px; line-height: 1.25; color: var(--ink);
    text-transform: uppercase; white-space: nowrap;
  }
  .flash svg { display: block; margin: 0 auto 6px; }

  .storage {
    position: absolute; left: 0; right: 0; top: 612px;
    text-align: center; font-weight: 700; font-size: 14px; color: var(--ink);
  }
  .net-weight {
    position: absolute; left: 0; right: 0; top: 654px;
    text-align: center; font-weight: 700; font-size: 18px; color: var(--ink);
  }
</style>
</head>
<body>
  <main class="bag">
    <svg class="bag__art" viewBox="0 0 500 720" width="500" height="720" aria-hidden="true">
      <rect x="0" y="0" width="500" height="50" fill="var(--seal)"/>
      <g stroke="var(--seal-line)" stroke-width="2">
        <line x1="0" y1="10" x2="500" y2="10"/><line x1="0" y1="18" x2="500" y2="18"/>
        <line x1="0" y1="26" x2="500" y2="26"/><line x1="0" y1="34" x2="500" y2="34"/>
        <line x1="0" y1="42" x2="500" y2="42"/>
      </g>
      <path d="M50 62 H450 V210 C380 206 330 190 250 204 C190 214 150 200 120 214 C95 226 70 240 50 238 Z" fill="var(--brand-blue)"/>
      <path d="M0 600 C120 540 250 490 500 430 V720 H0 Z" fill="var(--blush)"/>
      <path d="M0 600 C120 540 250 490 500 430" fill="none" stroke="var(--brand-blue)" stroke-width="8"/>
      <path d="M0 616 C120 556 250 506 500 446" fill="none" stroke="#fff" stroke-width="3" opacity="0.7"/>
      <path d="M110 690 V650 Q110 636 124 636 H420 Q440 636 440 616 V690 Z" fill="var(--deep-blue)"/>
      <rect x="0" y="690" width="500" height="30" fill="var(--seal)"/>
      <g stroke="var(--seal-line)" stroke-width="2">
        <line x1="0" y1="700" x2="500" y2="700"/><line x1="0" y1="710" x2="500" y2="710"/>
      </g>
    </svg>

    <div class="brand">
      <span class="brand__dot"></span>
      <span class="brand__name">Coral<br>Tide</span>
    </div>

    <p class="tagline">Shrimp you can trust<br>from pond to plate</p>

    <div class="window" role="img" aria-label="Product window showing peeled cooked shrimp"></div>
    <div class="cooked">COOKED</div>

    <div class="badge-natural" role="img" aria-label="All natural badge"></div>
    <div class="badge-small badge-small--origin" role="img" aria-label="Sourcing badge"></div>
    <div class="badge-small badge-small--packed" role="img" aria-label="Packed in USA badge"></div>

    <div class="flash">
      <svg width="34" height="34" viewBox="0 0 34 34" aria-hidden="true" stroke="var(--ink)" stroke-width="2.2" stroke-linecap="round">
        <line x1="17" y1="2" x2="17" y2="32"/><line x1="4" y1="9.5" x2="30" y2="24.5"/><line x1="4" y1="24.5" x2="30" y2="9.5"/>
        <polyline points="13,5 17,8 21,5" fill="none"/><polyline points="13,29 17,26 21,29" fill="none"/>
      </svg>
      Flash frozen to<br>lock in the flavor
    </div>

    <p class="storage">Keep Frozen – Do not refrigerate</p>
    <p class="net-weight">Net Wt. 1lbs</p>
  </main>
</body>
</html>
```